I'm looking for an app for customers to order through

I'm looking for an app for my customers to order products through
Ideally each customer would have a customer number with password
Their profile would come up with a preloaded products they currently order
From there they can select the product they require and volume needed for delivery
I would also like an option for them to go to a full product range if they are looking for Ideas or a product they don't currently use
Once the order is completed a copy of the order is them e-mailed to my distribution facilities and a confirmation sent to the customer by e-mail and/or SMS
Current product list is approx 1000 items
Current customers is 80 with expectations to expand to 200
On average current products ordered by each customer is is between 4-8 items
Ordering units are done by both weight and pieces/units

Target Market(s)

Food service outlets,
Restaurant , Hotels, catering companies, clubs, take away shops, cafes
Retail outlets

Number of Pages Required

1 page

Font styles to use
Sans Serif

Colors
abd037

Requirements
Must have
• Customer log in with Password 4 - 6 digit
• Customer order history
Nice to have
• Area for promotions / specials on a weekly / monthly basis

```html
<!DOCTYPE html>
<html lang="en">
<head>
<meta charset="utf-8">
<title>Profile Screen – Current Orders</title>
<link rel="stylesheet" href="https://fonts.googleapis.com/css2?family=Roboto:wght@400;500&display=swap">
<style>
  :root {
    --canvas-bg: #ececec;
    --header-bg: #151515;
    --surface: #ffffff;
    --accent: #abd037;
    --text-dark: #1a1a1a;
    --text-light: #ffffff;
    --text-muted: #8a8a8a;
    --label: #6f6f6f;
  }
  * { box-sizing: border-box; margin: 0; padding: 0; }
  html, body {
    width: 1000px;
    height: 1200px;
    overflow: hidden;
    background: var(--canvas-bg);
    font-family: "Roboto", Arial, sans-serif;
  }
  .app-screen {
    position: absolute;
    left: 200px;
    top: 68px;
    width: 600px;
    height: 1064px;
    background: var(--surface);
    overflow: hidden;
    box-shadow: 0 6px 24px rgba(0,0,0,0.12);
  }
  .profile-header {
    position: absolute;
    left: 0; top: 0;
    width: 100%;
    height: 182px;
    background: var(--header-bg);
    color: var(--text-light);
  }
  .status-bar {
    position: absolute;
    left: 0; top: 0;
    width: 100%;
    height: 33px;
    display: flex;
    align-items: center;
    justify-content: space-between;
    padding: 0 12px;
    font-size: 18px;
    font-weight: 500;
  }
  .status-left { display: flex; align-items: center; gap: 6px; }
  .status-right { display: flex; align-items: center; gap: 6px; }
  .status-time {
    position: absolute;
    left: 0; right: 0;
    text-align: center;
  }
  .menu-button {
    position: absolute;
    left: 24px;
    top: 51px;
  }
  .customer-name {
    position: absolute;
    left: 22px;
    top: 128px;
    font-size: 33px;
    font-weight: 400;
    letter-spacing: 0.2px;
  }
  .customer-avatar {
    position: absolute;
    left: 453px;
    top: 131px;
    width: 104px;
    height: 104px;
    border-radius: 50%;
    border: 4px solid var(--surface);
    background: radial-gradient(circle at 60% 40%, #5a5a5a 0%, #2c2c2c 55%, #d8d8d8 100%);
    box-shadow: 0 2px 6px rgba(0,0,0,0.35);
  }
  .section-label {
    position: absolute;
    left: 24px;
    top: 235px;
    font-size: 19px;
    color: var(--label);
    letter-spacing: 0.6px;
  }
  .order-list {
    position: absolute;
    left: 0; top: 300px;
    width: 100%;
    list-style: none;
  }
  .order-item {
    position: relative;
    height: 136.5px;
  }
  .order-thumb {
    position: absolute;
    left: 24px;
    top: 0;
    width: 96px;
    height: 96px;
    border-radius: 50%;
  }
  .thumb-apple  { background: radial-gradient(circle at 40% 40%, #e4453a, #a3161a 70%, #4c7a22); }
  .thumb-lamb   { background: linear-gradient(135deg, #e9dfe0, #a83c45 55%, #6b2830); }
  .thumb-burger { background: radial-gradient(circle at 50% 45%, #d48a2e, #7c3b16 55%, #1d1d1d 80%); }
  .thumb-banana { background: radial-gradient(circle at 50% 50%, #f7e02a, #d9b400 60%, #5a4a0a); }
  .thumb-ribs   { background: linear-gradient(135deg, #f1e4e6, #c5485a 55%, #7a1e2c); }
  .order-name {
    position: absolute;
    left: 143px;
    top: 14px;
    font-size: 30px;
    color: var(--text-dark);
  }
  .order-qty {
    position: absolute;
    left: 143px;
    top: 56px;
    font-size: 20px;
    color: var(--text-muted);
  }
  .order-price {
    position: absolute;
    right: 26px;
    top: 28px;
    font-size: 33px;
    color: var(--accent);
  }
</style>
</head>
<body>
  <main class="app-screen">
    <header class="profile-header">
      <div class="status-bar">
        <span class="status-time">9:41 AM</span>
        <span class="status-left">
          <svg width="52" height="10" viewBox="0 0 52 10" aria-hidden="true">
            <g fill="#ffffff">
              <circle cx="5" cy="5" r="4.5"/><circle cx="15" cy="5" r="4.5"/><circle cx="25" cy="5" r="4.5"/><circle cx="35" cy="5" r="4.5"/><circle cx="45" cy="5" r="4.5"/>
            </g>
          </svg>
          <span>Northwind</span>
          <svg width="20" height="15" viewBox="0 0 20 15" aria-hidden="true">
            <path d="M10 14 L6.5 10.5 A5 5 0 0 1 13.5 10.5 Z" fill="#fff"/>
            <path d="M3.5 7.5 A9 9 0 0 1 16.5 7.5" stroke="#fff" stroke-width="2" fill="none"/>
            <path d="M0.8 4.6 A13 13 0 0 1 19.2 4.6" stroke="#fff" stroke-width="2" fill="none"/>
          </svg>
        </span>
        <span class="status-right">
          <span>100%</span>
          <svg width="36" height="16" viewBox="0 0 36 16" aria-hidden="true">
            <rect x="0.5" y="0.5" width="31" height="15" rx="3" fill="none" stroke="#fff"/>
            <rect x="2.5" y="2.5" width="27" height="11" rx="1.5" fill="#fff"/>
            <rect x="33" y="5" width="2.5" height="6" rx="1" fill="#fff"/>
          </svg>
        </span>
      </div>
      <svg class="menu-button" width="41" height="32" viewBox="0 0 41 32" aria-label="Menu">
        <g stroke="var(--accent)" stroke-width="3">
          <line x1="0" y1="2" x2="41" y2="2"/>
          <line x1="0" y1="16" x2="41" y2="16"/>
          <line x1="0" y1="30" x2="41" y2="30"/>
        </g>
      </svg>
      <h1 class="customer-name">Marco Bellini</h1>
    </header>
    <div class="customer-avatar" role="img" aria-label="Customer profile photo"></div>

    <h2 class="section-label">CURRENT ORDERS</h2>
    <ul class="order-list">
      <li class="order-item">
        <div class="order-thumb thumb-apple" role="img" aria-label="Photo of red apples"></div>
        <span class="order-name">Apple</span>
        <span class="order-qty">1 dozen</span>
        <span class="order-price">$ 2.00</span>
      </li>
      <li class="order-item">
        <div class="order-thumb thumb-lamb" role="img" aria-label="Photo of lamb shoulder rack"></div>
        <span class="order-name">Lamb Shoulder Rack</span>
        <span class="order-qty">1 kilogram</span>
        <span class="order-price">$ 9.70</span>
      </li>
      <li class="order-item">
        <div class="order-thumb thumb-burger" role="img" aria-label="Photo of a hamburger"></div>
        <span class="order-name">Hamburger</span>
        <span class="order-qty">2 pieces</span>
        <span class="order-price">$ 5.49</span>
      </li>
      <li class="order-item">
        <div class="order-thumb thumb-banana" role="img" aria-label="Photo of bananas"></div>
        <span class="order-name">Banana</span>
        <span class="order-qty">1 kilogram</span>
        <span class="order-price">$ 3.90</span>
      </li>
      <li class="order-item">
        <div class="order-thumb thumb-ribs" role="img" aria-label="Photo of pork ribs"></div>
        <span class="order-name">Pork Ribs</span>
        <span class="order-qty">3 kilograms</span>
        <span class="order-price">$ 9.50</span>
      </li>
    </ul>
  </main>
</body>
</html>
```